Commercial Construction Company

We need a business card design based on our current logo. We are a commercial general contractor based in Southern California that specializes in bank remodels. We would like to see designs that incorporate dark blue. The final design should portray an image of professionalism and quality.

If possible, I would like to add metallic foil to the design. Thank you

```html
<!DOCTYPE html>
<html lang="en">
<head>
<meta charset="UTF-8">
<title>Halvern Build Group – Business Card</title>
<link href="https://fonts.googleapis.com/css2?family=Raleway:wght@400;500;600&display=swap" rel="stylesheet">
<style>
  :root {
    --backdrop: #8d8c8a;
    --card-white: #ffffff;
    --card-navy: #18274f;
    --brand-blue: #1d3f7c;
    --ink-grey: #6d6d6d;
    --foil-gold: #d9b445;
    --edge-blue: #bfe0f2;
  }
  * { margin: 0; padding: 0; box-sizing: border-box; }
  html, body { width: 1200px; height: 913px; overflow: hidden; }
  body {
    background: var(--backdrop);
    font-family: "Raleway", sans-serif;
    position: relative;
  }
  .card {
    position: absolute;
    width: 540px;
    height: 309px;
    border-radius: 3px;
    box-shadow: 0 10px 24px rgba(0,0,0,0.35);
  }
  .card-front {
    left: 70px; top: 120px;
    background: var(--card-white);
    box-shadow: 0 4px 0 var(--edge-blue), 0 12px 26px rgba(0,0,0,0.35);
  }
  .card-back {
    left: 590px; top: 484px;
    background: var(--card-navy);
  }
  .front-brand {
    position: absolute;
    left: 0; top: 0;
    width: 245px; height: 100%;
    display: flex; align-items: center; justify-content: center; gap: 10px;
  }
  .brand-dot {
    width: 14px; height: 14px; border-radius: 50%;
    background: var(--brand-blue);
  }
  .brand-name {
    font-weight: 600;
    font-size: 21px;
    letter-spacing: 0.5px;
    color: #161616;
    text-align: center;
    line-height: 1.15;
  }
  .divider {
    position: absolute;
    left: 250px; top: 70px;
    width: 1.5px; height: 170px;
    background: var(--brand-blue);
  }
  .contact-block {
    position: absolute;
    left: 272px; top: 62px;
    color: var(--ink-grey);
  }
  .person-name {
    font-size: 21px; font-weight: 500;
    color: var(--brand-blue);
    letter-spacing: 0.3px;
  }
  .person-role { font-size: 13px; margin-top: 2px; }
  .address { font-size: 12.5px; line-height: 1.35; margin-top: 22px; }
  .contact-list { list-style: none; margin-top: 16px; font-size: 12.5px; }
  .contact-list li { display: flex; align-items: center; gap: 9px; line-height: 1.55; }
  .contact-list svg { width: 12px; height: 12px; fill: var(--brand-blue); flex: none; }
  .back-brand {
    position: absolute; inset: 0;
    display: flex; align-items: center; justify-content: center; gap: 16px;
  }
  .back-brand .brand-dot { width: 22px; height: 22px; background: var(--foil-gold); }
  .back-brand .brand-name { color: var(--foil-gold); font-size: 34px; }
</style>
</head>
<body>
  <section class="card card-front">
    <div class="front-brand">
      <span class="brand-dot"></span>
      <span class="brand-name">Halvern<br>Build Group</span>
    </div>
    <div class="divider"></div>
    <div class="contact-block">
      <h1 class="person-name">DANIEL WHITFORD</h1>
      <p class="person-role">Director</p>
      <p class="address">2150 Meridian Park<br>Drive Suite 310,<br>Ontario, CA 91761</p>
      <ul class="contact-list">
        <li><svg viewBox="0 0 24 24"><path d="M6.6 10.8a15.1 15.1 0 0 0 6.6 6.6l2.2-2.2a1 1 0 0 1 1-.25 11.4 11.4 0 0 0 3.6.57 1 1 0 0 1 1 1V20a1 1 0 0 1-1 1A17 17 0 0 1 3 4a1 1 0 0 1 1-1h3.5a1 1 0 0 1 1 1c0 1.25.2 2.45.57 3.57a1 1 0 0 1-.25 1z"/></svg>9095550142</li>
        <li><svg viewBox="0 0 24 24"><path d="M2 5h20v14H2zm2 2v.5l8 5 8-5V7l-8 5z"/></svg>info@halvernbuild.com</li>
        <li><svg viewBox="0 0 24 24"><circle cx="12" cy="12" r="10"/></svg>www.halvernbuild.com</li>
      </ul>
    </div>
  </section>

  <section class="card card-back">
    <div class="back-brand">
      <span class="brand-dot"></span>
      <span class="brand-name">Halvern Build Group</span>
    </div>
  </section>
</body>
</html>
```